New Medical Practice Flyer/Announcement

Need a postcard size flyer for a new medical practice opening up. Need the medical provider's name and credentials, the office phone number, address and website on the inside. It is a unique holistic medical practice with a focus on kidney disease and eating disorders in addition to preventative health and diabetes/hypertension management. The look and design should be calming and natural with elements of elegance and sophistication.

Target Market(s)

Patients

Industry/Entity Type

Healthcare

Requirements
Must have
• Change to postcard format for direct mailing. Need logo in large print on front and back with address and Introduction.
Nice to have
• - The front of the postcard should have the logo in big print.
• - Back of postcard should have the script " Introducing a unique and customized medical practice to your health needs."
• - Dr. Marta Quillon, with credentials
• - Phone number and website
• - Email
• - Image of bubbles on the back of the card.

```html
<!DOCTYPE html>
<html lang="en">
<head>
<meta charset="utf-8">
<title>Stillwater Renal – Grand Opening</title>
<link href="https://fonts.googleapis.com/css2?family=Lexend:wght@300;400;600&family=Roboto+Condensed:wght@400&family=Yellowtail&family=Questrial&display=swap" rel="stylesheet">
<style>
:root{
  --navy:#27236b;
  --navy-deep:#221e63;
  --ink:#2b2866;
  --lavender-a:#d6d4f1;
  --lavender-b:#efecfd;
  --white:#ffffff;
  --stage:#5f6f6c;
}
*{margin:0;padding:0;box-sizing:border-box}
html,body{width:1200px;height:885px;overflow:hidden;background:var(--stage)}
.spread{position:absolute;left:0;top:18px;width:1325px;height:937px;transform:scale(0.9057);transform-origin:0 0;overflow:hidden;background:var(--navy)}

.panel-info{position:absolute;left:0;top:0;width:441px;height:937px;background:linear-gradient(90deg,var(--lavender-a),var(--lavender-b) 60%);color:var(--navy);font-family:"Lexend",sans-serif;padding:42px 48px 0 48px}
.panel-info h1{font-weight:600;font-size:25px;letter-spacing:-0.5px;line-height:30px;margin-bottom:4px}
.panel-info .intro{font-size:12.4px;font-weight:300;line-height:16px;text-align:justify;color:var(--ink);margin-bottom:14px}
.features{list-style:none;margin-top:18px}
.feature{display:flex;align-items:center;gap:12px;height:103px;border-bottom:1.5px solid var(--navy)}
.feature:first-child{height:88px;align-items:flex-start}
.feature.flip{flex-direction:row-reverse}
.feature .icon{flex:0 0 62px;height:62px;border-radius:50%;background:var(--navy);display:flex;align-items:center;justify-content:center}
.feature .text{flex:1}
.feature.flip .text{text-align:center}
.feature h2{font-size:16px;font-weight:600;letter-spacing:-0.2px;margin-bottom:2px}
.feature .desc{font-size:11.6px;font-weight:300;line-height:16px;color:var(--ink)}

.art{position:absolute;left:441px;top:0;width:884px;height:937px}
.fold{position:absolute;left:884px;top:0;width:1px;height:937px;background:rgba(0,0,0,.12)}

.contact{position:absolute;left:533px;top:479px;font-family:"Roboto Condensed",sans-serif;font-size:18px;color:var(--navy-deep);line-height:25px;list-style:none}
.contact li{display:flex;align-items:center;gap:6px}

.brand{position:absolute;left:930px;top:33px;width:395px;height:165px;background:var(--white);border-radius:82px 0 0 82px;display:flex;align-items:center;justify-content:center;gap:12px;padding-left:20px}
.brand .dot{width:14px;height:14px;border-radius:50%;background:#8fc7ea}
.brand .name{font-family:"Questrial",sans-serif;font-size:18px;letter-spacing:5px;color:var(--navy)}

.headline{position:absolute;left:1022px;top:418px;font-family:"Yellowtail",cursive;color:var(--navy);font-size:78px;line-height:60px;transform:rotate(-8deg)}
.headline span{display:block}
.headline .first{margin-left:58px}

.credentials{position:absolute;left:1050px;top:687px;width:200px;height:200px;border-radius:50%;background:rgba(255,255,255,.85);display:flex;align-items:center;justify-content:center;text-align:center;font-family:"Roboto Condensed",sans-serif;font-size:17px;line-height:24px;color:var(--navy-deep)}
</style>
</head>
<body>
<div class="spread">
  <svg class="art" viewBox="441 0 884 937" width="884" height="937">
    <defs>
      <linearGradient id="greenFill" x1="0" y1="0" x2="0" y2="1"><stop offset="0" stop-color="#8fd07f"/><stop offset="1" stop-color="#b6e9a2"/></linearGradient>
      <linearGradient id="mapFill" x1="0" y1="0" x2="1" y2="1"><stop offset="0" stop-color="#9ed3e2"/><stop offset=".5" stop-color="#e6e3dc"/><stop offset="1" stop-color="#a5d8e4"/></linearGradient>
      <linearGradient id="photoFill" x1="0" y1="0" x2="1" y2="1"><stop offset="0" stop-color="#a98760"/><stop offset="1" stop-color="#6d4e3a"/></linearGradient>
      <clipPath id="artClip"><rect x="441" y="0" width="884" height="937"/></clipPath>
    </defs>
    <g clip-path="url(#artClip)">
      <circle cx="878" cy="468" r="408" fill="url(#greenFill)"/>
      <circle cx="640" cy="205" r="225" fill="url(#mapFill)" role="img" aria-label="Street map showing the clinic location with a pin"/>
      <circle cx="1290" cy="545" r="290" fill="url(#photoFill)" role="img" aria-label="Photo of a laughing child with a parent outdoors"/>
      <circle cx="1140" cy="490" r="235" fill="#b6e9a2" opacity=".88"/>
    </g>
  </svg>
  <div class="fold"></div>

  <section class="panel-info">
    <h1>DR. MARTA QUILLON, MD</h1>
    <p class="intro">Introducing a unique and customized medical practice to your health needs. Stillwater Renal brings holistic, whole-person care to our community, pairing board-certified nephrology with thoughtful support for eating disorders. Every plan begins with listening: we take time to understand your history, your goals and your daily life before recommending treatment. Our calm, welcoming office helps you feel at ease from the first visit.</p>
    <p class="intro">Dr. Marta Quillon is board certified in Nephrology and Internal Medicine and specializes in kidney disease and eating disorders. She believes lasting health grows from prevention, nutrition and steady partnership. Visit us at 418 Alder Grove Road, Suite 210, Mesa Verde, AZ 85201, or call to schedule a new-patient consultation. Same-week appointments are often available.</p>
    <ul class="features">
      <li class="feature"><span class="icon"><svg width="34" height="34" viewBox="0 0 34 34" fill="none" stroke="#fff" stroke-width="1.8"><path d="M14 8c-6-3-10 3-9 9s6 10 9 7c2-2-1-5 0-8s2-6 0-8zM20 8c6-3 10 3 9 9s-6 10-9 7c-2-2 1-5 0-8s-2-6 0-8z"/></svg></span><div class="text"><h2>KIDNEY DISEASE CARE</h2><div class="desc">Early detection, chronic kidney disease management and dialysis planning, tailored to each stage of your journey.</div></div></li>
      <li class="feature flip"><span class="icon"><svg width="36" height="36" viewBox="0 0 36 36" fill="none" stroke="#fff" stroke-width="1.6"><circle cx="18" cy="14" r="8"/><path d="M4 22l6 8h6M32 22l-6 8h-6"/></svg></span><div class="text"><h2>EATING DISORDER SUPPORT</h2><div class="desc">Compassionate medical care for eating disorders, coordinated with your therapist and nutrition team.</div></div></li>
      <li class="feature"><span class="icon"><svg width="34" height="34" viewBox="0 0 34 34" fill="none" stroke="#fff" stroke-width="1.8"><path d="M17 29s-11-6.5-11-14a6 6 0 0 1 11-3.3A6 6 0 0 1 28 15c0 7.5-11 14-11 14z"/><path d="M10 17h4l2-4 3 7 2-3h3"/></svg></span><div class="text"><h2>PREVENTATIVE HEALTH</h2><div class="desc">Screenings, lab work and lifestyle guidance to catch concerns early and keep you feeling well.</div></div></li>
      <li class="feature flip"><span class="icon"><svg width="34" height="34" viewBox="0 0 34 34" fill="none" stroke="#fff" stroke-width="1.8"><path d="M17 5c5 7 8 11 8 15a8 8 0 0 1-16 0c0-4 3-8 8-15z"/></svg></span><div class="text"><h2>DIABETES MANAGEMENT</h2><div class="desc">Personalized plans for blood sugar control that protect your kidneys, heart and long-term health.</div></div></li>
      <li class="feature"><span class="icon"><svg width="36" height="36" viewBox="0 0 36 36" fill="none" stroke="#fff" stroke-width="1.6"><circle cx="18" cy="19" r="10"/><path d="M18 19l5-5M18 9v2M28 19h-2M10 19H8"/></svg></span><div class="text"><h2>HYPERTENSION CARE</h2><div class="desc">Blood pressure monitoring and gentle, sustainable treatment that fits your daily routine.</div></div></li>
    </ul>
  </section>

  <ul class="contact">
    <li><svg width="18" height="18" viewBox="0 0 18 18"><circle cx="9" cy="9" r="9" fill="#27236b"/><path d="M6 5l2 2-1 1.3c.6 1.2 1.5 2.1 2.7 2.7L11 10l2 2-1.4 1.4C8.5 13 5 9.5 4.6 6.4z" fill="#fff"/></svg>555.014.2290</li>
    <li><svg width="18" height="18" viewBox="0 0 18 18"><circle cx="9" cy="9" r="9" fill="#27236b"/><rect x="4.5" y="6" width="9" height="6.5" fill="#fff"/><path d="M4.5 6l4.5 3.5L13.5 6" stroke="#27236b" fill="none"/></svg>hello@stillwaterrenal.com</li>
    <li><svg width="18" height="18" viewBox="0 0 18 18"><circle cx="9" cy="9" r="9" fill="#27236b"/><g fill="none" stroke="#fff" stroke-width=".9"><circle cx="9" cy="9" r="4.5"/><ellipse cx="9" cy="9" rx="2" ry="4.5"/><path d="M4.5 9h9"/></g></svg>www.stillwaterrenal.com</li>
    <li><svg width="18" height="18" viewBox="0 0 18 18"><circle cx="9" cy="9" r="9" fill="#27236b"/><path d="M9 14s-3.5-4-3.5-6.3a3.5 3.5 0 0 1 7 0C12.5 10 9 14 9 14z" fill="#fff"/><circle cx="9" cy="7.7" r="1.2" fill="#27236b"/></svg>418 Alder Grove Rd, Suite 210, Mesa Verde, AZ</li>
  </ul>

  <div class="brand"><span class="dot"></span><span class="name">STILLWATER RENAL</span></div>

  <div class="headline"><span class="first">Grand</span><span>Opening</span></div>

  <div class="credentials">Nephrologist<br>and Eating Disorder<br>Specialist Board Certified,<br>Nephrology and Internal<br>Medicine</div>
</div>
</body>
</html>
```